Mini Leporello with Tartar Recipe from Christmas Apéro

As present from our christmas apero we would like to give our visitors a little booklet of the tartar recipes they enjoyed with us. For this we need a little pocket recipe booklet. ISt should be a Mini-Leparello. You can find the content attached.

Target Market(s)

customers christmas apero

Font styles to use
Other font styles liked:
• FS albert

Requirements
Must have
• each recipe comes from Kalmor or Markus Brenwil - it should show the author
• the format should be 85 x 85 mm and I need a printable file

```html
<!DOCTYPE html>
<html lang="de">
<head>
<meta charset="utf-8">
<title>Tartar-Rezepte vom Lumara Weihnachtsapéro 2016</title>
<link rel="stylesheet" href="https://fonts.googleapis.com/css2?family=Nunito+Sans:wght@400;700;800&family=Cormorant+Garamond:wght@500&display=swap">
<style>
:root{
  --stage:#c8c9cc;
  --paper:#161010;
  --paper-warm:#2a1a12;
  --ink:#ffffff;
  --ink-soft:#d9d4cf;
  --accent:#c8212c;
  --gold:#e0a83a;
  --amber:#b8661c;
}
*{box-sizing:border-box;margin:0;padding:0}
html,body{width:767px;height:1200px;overflow:hidden}
body{background:var(--stage);font-family:"Nunito Sans",Arial,sans-serif;color:var(--ink);position:relative}

.panel{position:absolute;background:
  radial-gradient(circle at 20% 15%,rgba(184,102,28,.18),transparent 40%),
  radial-gradient(circle at 85% 80%,rgba(200,33,44,.14),transparent 45%),
  var(--paper);overflow:hidden;box-shadow:0 6px 18px rgba(0,0,0,.35)}
.panel-frame{position:absolute;inset:12px;border:1.5px solid var(--ink);pointer-events:none}

/* cover */
.cover{left:183px;top:197px;width:400px;height:400px}
.cover-photo{position:absolute;inset:0;background:
  radial-gradient(circle at 30% 25%,rgba(224,168,58,.75),transparent 30%),
  radial-gradient(circle at 70% 35%,rgba(200,33,44,.45),transparent 28%),
  radial-gradient(circle at 50% 75%,rgba(184,102,28,.7),transparent 40%),
  linear-gradient(160deg,#3a2412,#120b08 70%)}
.cover-title{position:absolute;top:120px;left:0;right:0;text-align:center;text-transform:uppercase;font-weight:700;font-size:15px;line-height:1.25;letter-spacing:.3px}
.cover-year{display:block;font-family:"Cormorant Garamond",Georgia,serif;font-size:38px;font-weight:500;letter-spacing:2px;margin-top:4px;text-transform:none}
.brand{position:absolute;font-weight:800;letter-spacing:-.3px}
.cover .brand{left:0;right:0;top:298px;text-align:center;font-size:24px;line-height:1}
.brand-sub{display:block;font-size:6px;font-weight:400;letter-spacing:1.5px;margin-top:2px;text-transform:uppercase;margin-left:60px}
.url{position:absolute;font-size:7.5px;color:var(--ink-soft)}
.cover .url{left:0;right:0;bottom:20px;text-align:center}

/* recipe panels */
.recipes{top:637px;width:365px;height:365px;padding:26px 24px}
.recipes-left{left:10px}
.recipes-right{left:392px}
.recipe{margin-bottom:12px}
.recipe-title{display:inline-block;background:var(--accent);font-size:11px;font-weight:800;text-transform:uppercase;padding:3px 16px 3px 8px;border-radius:0 12px 12px 0;margin-left:-12px;letter-spacing:.3px}
.recipe-method{font-size:8.5px;margin:5px 0 4px;color:var(--ink-soft);line-height:1.35}
.ingredients{list-style:none;display:grid;grid-template-columns:repeat(3,1fr);gap:2px 8px;font-size:8px}
.ingredients li{display:flex;align-items:center;gap:4px}
.tick{width:8px;height:8px;background:var(--ink);flex:none;position:relative}
.tick::after{content:"";position:absolute;left:2.5px;top:.5px;width:2px;height:4.5px;border:solid var(--paper);border-width:0 1.5px 1.5px 0;transform:rotate(45deg)}
.author{position:absolute;top:22px;right:22px;display:flex;align-items:center;gap:4px;font-size:9px;font-weight:800}
.author-mark{width:12px;height:12px;background:var(--accent)}
.recipes .brand{right:24px;bottom:20px;font-size:12px;color:var(--accent)}
.recipes .url{left:24px;bottom:22px}
</style>
</head>
<body>

<section class="panel cover">
  <div class="cover-photo" role="img" aria-label="Weihnachtliches Bokeh-Foto mit Christbaumkugeln, Lichterketten, goldenen Sternen und Schneeflocken"></div>
  <div class="panel-frame"></div>
  <h1 class="cover-title">Tartar-Rezepte vom Lumara<br>Weihnachtsapéro<span class="cover-year">2016</span></h1>
  <div class="brand">Lumara<span class="brand-sub">IT Solutions</span></div>
  <div class="url">www.apero.lumara-it.ch</div>
</section>

<section class="panel recipes recipes-left">
  <div class="panel-frame"></div>
  <div class="author"><span class="author-mark"></span>Kalmor</div>

  <article class="recipe">
    <h2 class="recipe-title">Rindertartar</h2>
    <p class="recipe-method">Alle Zutaten fein hacken und mischen.</p>
    <ul class="ingredients">
      <li><span class="tick"></span>Rindsfilet</li><li><span class="tick"></span>Peperoni</li><li><span class="tick"></span>Eigelb</li>
      <li><span class="tick"></span>Essiggurken</li><li><span class="tick"></span>Kapern</li><li><span class="tick"></span>Salz</li>
      <li><span class="tick"></span>Oliven</li><li><span class="tick"></span>Zwiebel</li><li><span class="tick"></span>Pfeffer</li>
    </ul>
  </article>

  <article class="recipe">
    <h2 class="recipe-title">Ligurisches Kalbstartar</h2>
    <p class="recipe-method">Alle Zutaten fein hacken und mischen.</p>
    <ul class="ingredients">
      <li><span class="tick"></span>Kalbfleisch</li><li><span class="tick"></span>Knoblauch</li><li><span class="tick"></span>Salz</li>
      <li><span class="tick"></span>Zitronen</li><li><span class="tick"></span>Pinienkerne</li><li><span class="tick"></span>Gewürzsalz</li>
      <li><span class="tick"></span>Olivenöl</li><li><span class="tick"></span>Pfeffer</li><li><span class="tick"></span>Fenchelsamen</li>
    </ul>
  </article>

  <article class="recipe">
    <h2 class="recipe-title">Tomatentartar</h2>
    <p class="recipe-method">Tomaten kurz überbrühen, schälen, entkernen und fein würfeln. Mit den übrigen Zutaten mischen und kalt stellen.</p>
    <ul class="ingredients">
      <li><span class="tick"></span>Eigelb</li><li><span class="tick"></span>Cognac</li><li><span class="tick"></span>Salz</li>
      <li><span class="tick"></span>Kapern</li><li><span class="tick"></span>Pfeffer</li><li><span class="tick"></span>Basilikum</li>
    </ul>
  </article>

  <div class="url">www.apero.lumara-it.ch</div>
  <div class="brand">Lumara</div>
</section>

<section class="panel recipes recipes-right">
  <div class="panel-frame"></div>
  <div class="author"><span class="author-mark"></span>Kalmor</div>

  <article class="recipe">
    <h2 class="recipe-title">Thunatartar Asiatisch</h2>
    <p class="recipe-method">Dieses Thunatartar bekommt mit folgenden Zutaten eine asiatische Note. Fügen Sie weitere asiatische Saucen gemäss Ihrem Geschmack individuell bei.</p>
    <ul class="ingredients">
      <li><span class="tick"></span>Frühlingszwiebeln</li><li><span class="tick"></span>Ingwer</li><li><span class="tick"></span>Basilikum</li>
      <li><span class="tick"></span>Sojasauce</li><li><span class="tick"></span>Wasabi</li><li><span class="tick"></span>Pfeffer</li>
    </ul>
  </article>

  <article class="recipe">
    <h2 class="recipe-title">Lachstartar</h2>
    <p class="recipe-method">Geräucherten Lachs fein hacken und mit allen Zutaten mischen.</p>
    <ul class="ingredients">
      <li><span class="tick"></span>Geräucherter Lachs</li><li><span class="tick"></span>Schnittlauch</li><li><span class="tick"></span>Dill</li>
    </ul>
  </article>

  <article class="recipe">
    <h2 class="recipe-title">Käsetartar</h2>
    <p class="recipe-method">Den Käse und die Radieschen in kleine Würfel schneiden, Lauch fein hacken und alles gut vermischen.</p>
    <ul class="ingredients">
      <li><span class="tick"></span>Halbhartkäse</li><li><span class="tick"></span>Radieschen</li><li><span class="tick"></span>Petersilie</li>
      <li><span class="tick"></span>Weinessig</li><li><span class="tick"></span>Senf</li><li><span class="tick"></span>Lauch</li>
      <li><span class="tick"></span>Basilikum</li><li><span class="tick"></span>Salz</li><li><span class="tick"></span>Rapsöl</li>
      <li><span class="tick"></span>Rahm</li><li><span class="tick"></span>Schwarzer Pfeffer</li>
    </ul>
  </article>

  <div class="url">www.apero.lumara-it.ch</div>
  <div class="brand">Lumara</div>
</section>

</body>
</html>
```